Brivane Communications - veteran and exclusive boutique copywriting agency

PROJECT NEEDS:
1. Website design - full homepage design and inner page top banner design
2. Logo design
* Please see attached Briefs (Word Docs) for descriptions of what is needed for 1 and 2 above.
ABOUT THE CLIENT:
Brivane Communications is a veteran and exclusive boutique copywriting agency run by Martin Olafsky. Martin is an award-winning published novelist and an accomplished executive ghostwriter with articles regularly published prominent technology publications like Pulsar, ByteHarbor, CapitalDrift, and more. For nearly three decades, Martin has focused solely on the technology sector - serving clients in Israel, Europe and the US.

Target Market(s)

hi-tech companies run by serious, confident professionals.

Industry/Entity Type

Business

Number of Pages Required

2 page

Font styles to use
Sans Serif
Other font styles liked:
• font should be modern

Colors
0054AA
0677BA
7BADD7
CADEEF
E8F1F8
F0912C
F2A743
F7CA91
FBE8D2
FDF5EE

Requirements
Must have
• psd files for logo, homepage design, and inner page top banner design
Nice to have
• Please see attached Website and Logo Design Briefs (Word Docs)
Should not have

```html
<!DOCTYPE html>
<html lang="en">
<head>
<meta charset="utf-8">
<title>Brivane Communications</title>
<link href="https://fonts.googleapis.com/css2?family=Barlow+Condensed:wght@400;600&family=Barlow+Semi+Condensed:wght@600&family=Noto+Serif:wght@400&family=Montserrat:wght@700;800&display=swap" rel="stylesheet">
<style>
:root{
  --hero-blue:#0a56c2;
  --hero-dark:#1f232c;
  --headline:#e2dea6;
  --cream:#f6f6ec;
  --rule-blue:#0a55c4;
  --title-blue:#1c5cbf;
  --ink:#2a2a2a;
  --highlight:#f4b3a4;
  --panel-yellow:#fecb24;
  --panel-green:#d9e6b0;
  --panel-steel:#a5bcd9;
  --rule-coral:#f0735a;
  --bright-blue:#0b6cef;
  --footer:#1e2028;
  --button:#dfe6b0;
  --white:#ffffff;
}
*{margin:0;padding:0;box-sizing:border-box}
html,body{width:1200px;height:2576px;overflow:hidden}
body{position:relative;font-family:"Noto Serif",serif;background:var(--footer);color:var(--ink)}
.abs{position:absolute}
.hero{left:0;top:0;width:1200px;height:660px;background:var(--hero-dark);overflow:hidden}
.portrait{left:620px;top:30px;width:560px;height:630px;background:radial-gradient(ellipse at 55% 40%,#9fbbe0 0%,#6f93c8 45%,#2f3b52 80%,transparent 100%)}
.brand{left:246px;top:18px;color:var(--white);font-family:"Montserrat",sans-serif}
.brand-name{font-size:30px;font-weight:800;letter-spacing:1px;line-height:1}
.brand-sub{font-size:8px;font-weight:700;letter-spacing:.6px;margin-top:3px}
.nav{left:565px;top:28px;display:flex;gap:18px;font-size:13px;color:var(--white)}
.headline{left:246px;top:205px;font-family:"Barlow Semi Condensed",sans-serif;font-weight:600;font-size:86px;line-height:80px;color:var(--headline);letter-spacing:-1px}
.lede{left:246px;top:383px;width:380px;font-size:20px;line-height:27.5px;color:var(--white)}
.cream{left:0;top:660px;width:1200px;height:465px;background:var(--cream)}
.logos{left:177px;top:614px;width:846px;height:158px;background:var(--white);display:flex;align-items:center;justify-content:space-around;padding:0 50px}
.logo-name{font-family:"Noto Serif",serif;font-size:22px;color:#4a4a4a}
.intro-title{left:303px;top:846px;font-size:28px;color:var(--title-blue)}
.intro-text{left:307px;top:892px;width:510px;font-size:22px;line-height:31.5px;color:var(--ink)}
.tagline{left:303px;top:1010px;font-size:16px;padding:0 4px;background:linear-gradient(transparent 68%,var(--highlight) 68%)}
.rule{left:0;width:1200px;height:6px}
.panel{top:1131px;width:400px;height:494px}
.panel-art{left:60px;top:70px;width:290px;height:230px;border-radius:6px}
.panel-title{left:75px;top:330px;width:280px;font-size:27px;line-height:34px;color:#1d1d1d}
.testimonials{left:0;top:1631px;width:1200px;height:560px;background:var(--bright-blue);overflow:hidden}
.t-title{left:245px;top:82px;font-size:42px;line-height:53px;color:var(--white)}
.t-line{left:570px;top:163px;width:321px;height:2px;background:var(--white)}
.quote{left:350px;top:268px;width:525px;font-size:18px;line-height:25px;color:var(--white)}
.cite{left:350px;top:418px;font-size:12px;color:var(--white)}
.qmark{left:277px;top:288px;font-family:"Montserrat",sans-serif;font-weight:800;font-size:80px;line-height:80px;color:#1a5fc8}
.cta{left:0;top:2268px;width:1200px;text-align:center;font-family:"Barlow Condensed",sans-serif;font-size:40px;color:var(--white)}
.button{left:541px;top:2331px;width:114px;height:30px;background:var(--button);font-size:13px;line-height:30px;text-align:center;color:#333}
.f-line{left:246px;top:2387px;width:712px;height:1px;background:#3a3d45}
.contact{left:0;top:2419px;width:1200px;text-align:center;font-size:11px;line-height:19px;color:#d8d8d8}
.social{left:557px;top:2487px;display:flex;gap:8px}
.social span{width:23px;height:23px;border-radius:50%;background:var(--white);display:block}
</style>
</head>
<body>
<div class="abs hero">
  <div class="abs portrait" role="img" aria-label="Portrait photograph of Martin Olafsky in a light blue shirt against a dark backdrop"></div>
  <svg class="abs" style="left:0;top:0" width="1200" height="660" viewBox="0 0 1200 660">
    <path d="M0 0H410C430 60 520 110 610 150C690 190 720 280 690 340C660 400 640 460 655 520C665 580 690 620 700 660H0Z" fill="var(--hero-blue)"/>
    <defs><linearGradient id="ringA" x1="0" y1="0" x2="1" y2="1"><stop offset="0" stop-color="#7eb3e0"/><stop offset="1" stop-color="#d8ecef"/></linearGradient></defs>
    <circle cx="95" cy="668" r="167" fill="none" stroke="url(#ringA)" stroke-width="66"/>
  </svg>
  <div class="abs brand"><div class="brand-name">Brivane</div><div class="brand-sub">COMMUNICATIONS</div></div>
  <nav class="abs nav"><span>About</span><span>Services</span><span>Industries</span><span>Portfolio</span><span>Clients</span><span>Contact</span></nav>
  <h1 class="abs headline">Your voice,<br>my words</h1>
  <p class="abs lede">Copywriting and executive ghostwriting that speaks for your vision and your technology.</p>
</div>

<div class="abs cream">
  <svg class="abs" style="left:0;top:0" width="300" height="200" viewBox="0 0 300 200"><path d="M0 130A167 167 0 0 0 262 8" fill="none" stroke="#e4ecea" stroke-width="66"/></svg>
</div>
<div class="abs logos">
  <span class="logo-name">Nestora</span><span class="logo-name">Quillon</span><span class="logo-name">Veltrix</span><span class="logo-name">Fabrisoft</span><span class="logo-name">Brightwell</span>
</div>
<h2 class="abs intro-title">The Words that Launch the Conversation</h2>
<p class="abs intro-text">In a crowded marketspace, your messages need to engage. Your offering needs to rise above the background noise -but not by shouting.</p>
<p class="abs tagline">It's the art of business communication.</p>

<div class="abs rule" style="top:1125px;background:var(--rule-blue)"></div>
<section class="abs panel" style="left:0;background:var(--panel-yellow)">
  <div class="abs panel-art" style="background:radial-gradient(circle,#fde58c,var(--panel-yellow) 70%)" role="img" aria-label="Illustration of a megaphone with speech bubbles and a rising bar chart"></div>
  <h3 class="abs panel-title">The Value of a Fresh Perspective</h3>
</section>
<section class="abs panel" style="left:400px;background:var(--panel-green)">
  <div class="abs panel-art" style="background:linear-gradient(135deg,#1f5e4a 0%,#f2f4ee 45%,#ffffff 100%);opacity:.8" role="img" aria-label="Stationery set with business cards, envelope and letterhead in green and white"></div>
  <h3 class="abs panel-title">Concise, Eloquent, Effective - Always Creative</h3>
</section>
<section class="abs panel" style="left:800px;background:var(--panel-steel)">
  <div class="abs panel-art" style="background:linear-gradient(160deg,#dfe8f2,#8fb1e3 60%,var(--panel-steel))" role="img" aria-label="Illustration of a person working beside a large web page layout"></div>
  <h3 class="abs panel-title" style="left:64px">Giving Voice to Your Vision</h3>
</section>
<div class="abs rule" style="top:1625px;background:var(--rule-coral)"></div>

<section class="abs testimonials">
  <svg class="abs" style="left:0;top:0" width="1200" height="560" viewBox="0 0 1200 560">
    <defs><linearGradient id="ringB" x1="0" y1="0" x2="1" y2="1"><stop offset="0" stop-color="#6fd0f7"/><stop offset="1" stop-color="#1f7df2"/></linearGradient></defs>
    <circle cx="307" cy="339" r="101" fill="none" stroke="url(#ringB)" stroke-width="42"/>
    <path d="M1200 380C1150 400 1100 440 1095 500C1093 530 1100 550 1110 560H1200Z" fill="#0a55cc"/>
  </svg>
  <h2 class="abs t-title">What our clients say<br>about our work</h2>
  <div class="abs t-line"></div>
  <div class="abs qmark">“</div>
  <p class="abs quote">We've continued to work Martin over the years because he excels at turning ideas into viable and compelling marketing content that really reaches our target audience. His experience in the security field has also been a big plus for Shieldora, and has enabled him to add real value to our company.</p>
  <p class="abs cite">Noa Keller, Director of Marketing,Shieldora (Ardentis)</p>
</section>

<svg class="abs" style="left:0;top:2190px" width="1200" height="386" viewBox="0 0 1200 386">
  <path d="M1200 0H1110C1115 40 1125 80 1120 120C1110 160 1080 200 1090 240C1105 280 1160 270 1200 262Z" fill="#0a55cc"/>
  <circle cx="69" cy="259" r="9" fill="none" stroke="#555a63" stroke-width="2"/>
  <circle cx="80" cy="386" r="45" fill="none" stroke="#3a3d45" stroke-width="12"/>
</svg>
<h2 class="abs cta">Lets work on your next project together .</h2>
<div class="abs button">Contact Brivane</div>
<div class="abs f-line"></div>
<p class="abs contact">You can contact Brivane Communications by dialing&nbsp; +972-50-000-1234. You may also mail us at hello@brivane.example<br>© 2023 Brivane Communications. All Rights Reserved.</p>
<div class="abs social" aria-label="Social links"><span></span><span></span><span></span></div>
</body>
</html>
```